Tri fold brochure for construction company

Looking for a tri fold brochure which utilizes black, teal and white colors. Logo must be on main page (several files with Logo attached)
Inside brochure.
1st Page - 3D photo/sketch/drawing of a complete residential high rise building with windows, balconies and elements of concrete and bricks.
2nd Page - Text which will outline company's main activities. file with text is attached.
3rd Page - photo/sketch/drawing of underground parking garage which shows columns/beams/walls/ and garage entrance/exit ramp. Can be multiple photos.
Back of brochure
1st page - company logo
2nd page - please propose something.
3rd page - company message with address and contact info (to be provided)
Back ground color of brochure should complement our logo/photos/sketches/drawings.
Alternative design options are welcome.

```html
<!DOCTYPE html>
<html lang="en">
<head>
<meta charset="utf-8">
<title>Northvale Restoration Corp – Tri-fold Brochure</title>
<link href="https://fonts.googleapis.com/css2?family=Open+Sans:wght@300;400;600;700&display=swap" rel="stylesheet">
<style>
  :root {
    --stage: #6e6a6a;
    --paper: #f1f1f1;
    --teal: #22a88b;
    --band: #5b5b5b;
    --ink: #4a4a4a;
    --pill: #3b3b3b;
    --white: #ffffff;
  }
  * { box-sizing: border-box; margin: 0; padding: 0; }
  html, body { width: 1200px; height: 800px; overflow: hidden; }
  body {
    background: var(--stage);
    font-family: "Open Sans", Arial, sans-serif;
    position: relative;
  }
  .brochure {
    position: absolute;
    left: 90px; top: 60px;
    width: 1020px; height: 680px;
    background: var(--paper);
    box-shadow: 0 12px 30px rgba(0,0,0,.35);
    overflow: hidden;
  }
  .layer { position: absolute; inset: 0; width: 1020px; height: 680px; }
  .panel { position: absolute; top: 0; width: 340px; height: 680px; }
  .panel--left { left: 0; }
  .panel--middle { left: 340px; }
  .panel--right { left: 680px; }

  /* Left panel */
  .services { position: absolute; left: 26px; right: 26px; top: 322px; color: var(--white); }
  .services h3 { font-size: 13px; font-weight: 700; line-height: 1.3; margin-bottom: 6px; }
  .services p { font-size: 10px; line-height: 1.5; margin-bottom: 16px; opacity: .95; }

  /* Middle panel */
  .about { position: absolute; left: 34px; right: 34px; top: 40px; text-align: center; }
  .about h3 { color: var(--teal); font-size: 12px; font-weight: 700; text-transform: uppercase; margin-bottom: 6px; letter-spacing: .3px; }
  .about p { color: var(--ink); font-size: 9.5px; line-height: 1.5; margin-bottom: 18px; }
  .contact { position: absolute; left: 0; right: 0; top: 412px; text-align: center; color: var(--white); }
  .contact h2 { font-size: 18px; font-weight: 400; margin-bottom: 20px; }
  .contact-item { margin-bottom: 18px; font-size: 12px; }
  .contact-icon { display: block; width: 16px; height: 16px; margin: 0 auto 6px; }

  /* Right panel */
  .brand { position: absolute; left: 40px; top: 26px; display: flex; align-items: center; gap: 12px; }
  .brand-mark { width: 30px; height: 30px; background: var(--teal); }
  .brand-name { color: var(--teal); font-weight: 700; font-size: 17px; line-height: 1.15; text-transform: uppercase; letter-spacing: .5px; }
  .tagline { position: absolute; left: 0; right: 0; top: 410px; text-align: center; color: var(--white); text-transform: uppercase; }
  .tagline-strong { font-size: 19px; font-weight: 700; letter-spacing: .3px; }
  .tagline-light { font-size: 19px; font-weight: 300; letter-spacing: .3px; }
  .web-pill {
    position: absolute; right: 24px; top: 490px;
    background: var(--pill); color: var(--white);
    font-size: 10px; padding: 4px 14px; border-radius: 10px;
  }
</style>
</head>
<body>
<main class="brochure">
  <svg class="layer" viewBox="0 0 1020 680" aria-hidden="true">
    <path d="M0,300 Q170,285 340,305 L340,680 L0,680 Z" fill="var(--teal)"/>
    <path d="M340,360 Q510,330 680,372 L680,392 Q510,352 340,380 Z" fill="var(--band)"/>
    <path d="M340,376 Q510,346 680,388 L680,680 L340,680 Z" fill="var(--teal)"/>
    <path d="M680,322 Q850,378 1020,318 L1020,346 Q850,404 680,348 Z" fill="var(--band)"/>
    <path d="M680,344 Q850,400 1020,342 L1020,680 L680,680 Z" fill="var(--teal)"/>
    <path d="M680,82 Q850,60 1020,86 L1020,96 Q850,70 680,92 Z" fill="var(--band)"/>
    <line x1="340" y1="0" x2="340" y2="680" stroke="rgba(0,0,0,.08)" stroke-width="1"/>
    <line x1="680" y1="0" x2="680" y2="680" stroke="rgba(0,0,0,.08)" stroke-width="1"/>
  </svg>

  <svg class="layer" viewBox="0 0 1020 680" role="img" aria-label="Photo of construction workers in hard hats and safety vests looking up at a high-rise under construction with a crane">
    <defs>
      <linearGradient id="siteSky" x1="0" y1="0" x2="0" y2="1">
        <stop offset="0" stop-color="#2f6fb5"/>
        <stop offset=".55" stop-color="#8fb3d6"/>
        <stop offset="1" stop-color="#6b6a5e"/>
      </linearGradient>
    </defs>
    <path d="M0,0 H340 V300 Q170,280 0,295 Z" fill="url(#siteSky)"/>
  </svg>

  <svg class="layer" viewBox="0 0 1020 680" role="img" aria-label="Photo of glass office towers at dusk with lit windows and light trails on a curved road">
    <defs>
      <linearGradient id="cityDusk" x1="0" y1="0" x2="1" y2="1">
        <stop offset="0" stop-color="#1d3550"/>
        <stop offset=".6" stop-color="#2f4b66"/>
        <stop offset="1" stop-color="#6b5a3a"/>
      </linearGradient>
    </defs>
    <path d="M680,92 Q850,70 1020,96 L1020,320 Q850,380 680,324 Z" fill="url(#cityDusk)"/>
  </svg>

  <section class="panel panel--left">
    <div class="services">
      <h3>Sit Voluptatem<br>Accusantium Doloremque Laudantium</h3>
      <p>Totam rem aperiam, eaque ipsa quae ab illo inventore veritatis et quasi architecto beatae vitae dicta sunt explicabo. Nemo enim ipsam voluptatem quia voluptas sit aspernatur aut odit aut fugit, sequi nesciunt.</p>
      <h3>Ut Enim Ad Minima Veniam</h3>
      <p>Quis nostrum exercitationem ullam corporis suscipit laboriosam, nisi ut aliquid ex ea commodi consequatur? Quis autem vel eum iure reprehenderit qui in ea voluptate velit esse quam nihil.</p>
      <h3>Vero Eos Et Accusamus</h3>
      <p>Et iusto odio dignissimos ducimus qui blanditiis praesentium voluptatum deleniti atque corrupti quos dolores et quas molestias excepturi sint occaecati, id est laborum et dolorum fuga.</p>
    </div>
  </section>

  <section class="panel panel--middle">
    <div class="about">
      <h3>Cum Soluta Nobis</h3>
      <p>Est eligendi optio cumque nihil impedit quo minus id quod maxime placeat facere possimus, omnis voluptas assumenda est. Temporibus autem quibusdam et aut officiis debitis aut rerum necessitatibus.</p>
      <h3>Tenetur a Sapiente Delectus</h3>
      <p>Sed ut perspiciatis unde omnis iste natus error sit voluptatem accusantium doloremque laudantium, totam rem aperiam, eaque ipsa quae ab illo inventore veritatis et quasi architecto beatae.</p>
      <h3>Eius Modi Tempora</h3>
      <p>Incidunt ut labore et dolore magnam aliquam quaerat voluptatem. Ut enim ad minima veniam, quis nostrum exercitationem ullam corporis suscipit laboriosam.</p>
    </div>

    <div class="contact">
      <h2>Contact Us</h2>
      <div class="contact-item">
        <svg class="contact-icon" viewBox="0 0 16 16" aria-hidden="true">
          <circle cx="8" cy="8" r="8" fill="var(--pill)"/>
          <path d="M5.2,4.2 L6.6,4 L7.3,5.8 L6.5,6.5 Q7.2,8.4 9.5,9.5 L10.2,8.7 L12,9.4 L11.8,10.8 Q7.8,11.6 4.5,6.5 Q4.6,5 5.2,4.2 Z" fill="var(--white)"/>
        </svg>
        0155-372-904
      </div>
      <div class="contact-item">
        <svg class="contact-icon" viewBox="0 0 16 16" aria-hidden="true">
          <circle cx="8" cy="8" r="8" fill="var(--pill)"/>
          <circle cx="8" cy="8" r="4.2" fill="none" stroke="var(--white)" stroke-width="1"/>
          <path d="M3.8,8 H12.2 M8,3.8 Q5.6,8 8,12.2 M8,3.8 Q10.4,8 8,12.2" fill="none" stroke="var(--white)" stroke-width=".8"/>
        </svg>
        www.northvalerestoration.com
      </div>
      <div class="contact-item">
        <svg class="contact-icon" viewBox="0 0 16 16" aria-hidden="true">
          <circle cx="8" cy="8" r="8" fill="var(--pill)"/>
          <rect x="4" y="5.2" width="8" height="5.6" fill="none" stroke="var(--white)" stroke-width="1"/>
          <path d="M4,5.2 L8,8.4 L12,5.2" fill="none" stroke="var(--white)" stroke-width="1"/>
        </svg>
        info@northvalerestoration.com
      </div>
    </div>
  </section>

  <section class="panel panel--right">
    <div class="brand">
      <span class="brand-mark"></span>
      <span class="brand-name">Northvale<br>Restoration Corp</span>
    </div>
    <div class="tagline">
      <div class="tagline-strong">Sed ut perspiciatis unde</div>
      <div class="tagline-light">Omnis iste natus error</div>
    </div>
    <div class="web-pill">www.northvalerestoration.com</div>
  </section>
</main>
</body>
</html>
```